Business card for builder specialising in renovations.

Need a card for our building business. Business name is under Marcus Pellow.
Have licence number on card ( 527196K)
Contact number (0400 583 214)
Want to work on logo for some business cards and shirts - something with MP or MPB or open to ideas??
No animations, No hammers. Something sharp and eye catching.
Highlight that we are a renovation specialist. Simple on front with extra details on back with some lines to jot down things.

Target Market(s)

Renovators

Industry/Entity Type

Building

Contact Information for Business Card

2 sided with room on back to jot things down.
Extra details on back so front can be simple ..like, renovations, bathrooms, decks, extensions, new builds,

Logo Text

MP

Font styles to use
Serif

Requirements
Must have
• Eye catching design .
• Name : Marcus pellow
• Licence number
• Contact number - 0400583214
Nice to have
• Some logo design that we can carry through to other forms of advertising
• Local builder
• Quality work
Should not have
• No animations

```html
<!DOCTYPE html>
<html lang="en">
<head>
<meta charset="utf-8">
<title>Marcus Pellow – Business Card</title>
<link rel="stylesheet" href="https://fonts.googleapis.com/css2?family=Tinos:wght@400;700&display=swap">
<style>
  :root {
    --backdrop: #2b2b2d;
    --card-dark: #000000;
    --card-light: #ffffff;
    --brand-blue: #29a8e0;
    --ink: #111111;
    --paper-text: #ffffff;
  }
  * { box-sizing: border-box; margin: 0; padding: 0; }
  html, body {
    width: 1200px; height: 900px; overflow: hidden;
    background: var(--backdrop);
    font-family: "Tinos", "Times New Roman", serif;
  }
  .canvas { position: relative; width: 1200px; height: 900px; }

  .card {
    position: absolute; width: 700px; height: 400px;
    border-radius: 26px; overflow: hidden;
  }

  /* Front */
  .card-front { left: 90px; top: 50px; background: var(--card-dark); color: var(--paper-text); }
  .front-mark {
    position: absolute; left: 0; right: 0; top: 70px;
    display: flex; align-items: center; justify-content: center; gap: 16px;
  }
  .mark-square { width: 26px; height: 26px; background: var(--brand-blue); }
  .mark-initials { font-size: 96px; font-weight: 700; color: var(--brand-blue); letter-spacing: 4px; line-height: 1; }
  .front-name {
    position: absolute; left: 0; right: 0; top: 190px; text-align: center;
    font-size: 34px; font-weight: 700; letter-spacing: 3px; color: var(--brand-blue);
  }
  .front-web {
    position: absolute; left: 0; right: 0; top: 250px; text-align: center;
    font-size: 19px; letter-spacing: 1px;
  }
  .front-web .accent { color: var(--brand-blue); }
  .service-pill {
    position: absolute; left: 60px; right: 60px; top: 300px; height: 32px;
    border: 2px solid var(--brand-blue); border-radius: 16px;
    display: flex; align-items: center; justify-content: center;
    font-size: 16px; letter-spacing: 0.6px;
  }

  /* Back */
  .card-back { left: 410px; top: 470px; background: var(--card-light); color: var(--ink); }
  .back-tab { position: absolute; right: 0; top: 0; width: 22px; height: 34px; background: var(--brand-blue); }
  .back-name {
    position: absolute; right: 34px; top: 18px; text-align: right;
    font-size: 24px; color: var(--brand-blue); letter-spacing: 0.5px;
  }
  .back-role { position: absolute; right: 34px; top: 48px; font-size: 14px; }
  .rule { position: absolute; height: 1.5px; background: var(--ink); }
  .rule-top { left: 150px; right: 30px; top: 150px; }
  .rule-bottom { left: 150px; right: 30px; top: 340px; }
  .back-mark {
    position: absolute; left: 40px; top: 200px;
    display: flex; align-items: center; gap: 10px;
  }
  .back-mark .mark-square { width: 18px; height: 18px; }
  .back-mark .mark-initials { font-size: 70px; }
  .contact-list {
    position: absolute; right: 30px; top: 175px; list-style: none;
    text-align: right; font-size: 16px; line-height: 25px;
  }
  .contact-list li { display: flex; justify-content: flex-end; align-items: center; gap: 8px; }
  .contact-list .accent { color: var(--brand-blue); }
  .icon { width: 13px; height: 13px; fill: none; stroke: var(--brand-blue); stroke-width: 2; }
  .icon-spacer { width: 13px; }
</style>
</head>
<body>
<main class="canvas">
  <section class="card card-front">
    <div class="front-mark">
      <span class="mark-square"></span>
      <span class="mark-initials">MP</span>
    </div>
    <div class="front-name">MARCUS PELLOW</div>
    <div class="front-web">www.<span class="accent">marcuspellow</span>.com</div>
    <div class="service-pill">RENOVATIONS, BATHROOMS, DECKS, EXTENSIONS, NEW BUILDS,</div>
  </section>

  <section class="card card-back">
    <span class="back-tab"></span>
    <div class="back-name">MARCUS PELLOW</div>
    <div class="back-role">Director</div>
    <div class="rule rule-top"></div>
    <div class="back-mark">
      <span class="mark-square"></span>
      <span class="mark-initials">MP</span>
    </div>
    <ul class="contact-list">
      <li>Licence: (527196K)<span class="icon-spacer"></span></li>
      <li>0400583214
        <svg class="icon" viewBox="0 0 24 24"><path d="M5 3h4l2 5-3 2a12 12 0 0 0 6 6l2-3 5 2v4a2 2 0 0 1-2 2A18 18 0 0 1 3 5a2 2 0 0 1 2-2z"/></svg>
      </li>
      <li>info@marcuspellow.com
        <svg class="icon" viewBox="0 0 24 24"><rect x="2" y="5" width="20" height="14"/><path d="M2 5l10 8 10-8"/></svg>
      </li>
      <li>www.<span class="accent">marcuspellow</span>.com
        <svg class="icon" viewBox="0 0 24 24"><circle cx="12" cy="12" r="10"/><path d="M2 12h20M12 2c3 3 3 17 0 20M12 2c-3 3-3 17 0 20"/></svg>
      </li>
    </ul>
    <div class="rule rule-bottom"></div>
  </section>
</main>
</body>
</html>
```